Beautiful Simple and Clean WEbsite for Life Coach

Looking for a simple clean site website for life coach for educators. A home page will have an embedded opt-in form, menu bar will be
Work With Me - page for my coaching program and link to online calendar for booking
PRAISE - testimonials
ABOUT
PODCAST
I can supply images and a site I would like it modeled after is https://tessabrook.com/
My current website at www.danawhitfield.com is too dark. I am looking for the white space, pink and magenta. Feel free to use images from the site

Industry/Entity Type

Life Coaching

Number of Pages Required

4 page

Font styles to use
Serif

Colors
E54698
E96AAD
F1A4CE
F9D9EA
FCEFF6

Requirements
Must have
• See attached files for must-haves, Lots of white space, opt-in from for freebie is the most prominent on home page
Nice to have
• refer to Tessa Brook websites
Should not have
• dark colors, any balck background

```html
<!DOCTYPE html>
<html lang="en">
<head>
<meta charset="utf-8">
<title>Dana Whitfield — Life Coach for Educators</title>
<link href="https://fonts.googleapis.com/css2?family=Playfair+Display:wght@400;500&family=Work+Sans:wght@400;500;600&display=swap" rel="stylesheet">
<style>
:root{
  --magenta:#E54698;
  --pink:#E96AAD;
  --rose:#F4A3B8;
  --pink-soft:#F1A4CE;
  --blush:#F9D9EA;
  --blush-pale:#FCEFF6;
  --sage:#DCE3DE;
  --grey-panel:#EEF1EF;
  --mauve:#9C7E86;
  --ink:#3A3A3A;
  --muted:#6B6B6B;
  --white:#FFFFFF;
  --serif:"Playfair Display", Georgia, serif;
  --sans:"Work Sans", Arial, sans-serif;
}
*{box-sizing:border-box;margin:0;padding:0}
html,body{width:1200px;height:4152px;overflow:hidden}
body{position:relative;background:var(--white);font-family:var(--sans);color:var(--ink)}
.abs{position:absolute}
.topline{left:0;top:0;width:1200px;height:5px;background:var(--pink-soft)}
/* header */
.brand{left:78px;top:22px;font-family:var(--serif);font-size:30px;color:var(--pink);letter-spacing:.5px}
.nav{top:44px;font-size:15px;letter-spacing:1.5px;text-transform:uppercase;color:var(--muted)}
.nav.active{color:var(--pink)}
.book-online{left:944px;top:34px;width:122px;height:40px;background:var(--sage);font-size:13px;letter-spacing:1px;display:flex;align-items:center;justify-content:center;color:var(--ink)}
/* hero */
.photo{background:linear-gradient(135deg,#c9b79a,#8f8063 45%,#3e5f96 70%,#c6b08e);}
.hero-photo{left:525px;top:146px;width:675px;height:505px}
.hero-shadow{left:58px;top:218px;width:516px;height:360px;background:var(--blush-pale)}
.hero-box{left:76px;top:200px;width:516px;height:360px;background:var(--rose);padding:80px 40px 0 64px;color:var(--white)}
.hero-title{font-family:var(--serif);font-size:38px;line-height:1.1;letter-spacing:2px;text-transform:uppercase;font-weight:400}
.hero-sub{font-size:14px;line-height:1.5;margin-top:22px;opacity:.95}
.btn-outline{display:inline-flex;align-items:center;justify-content:center;border:1px solid currentColor;font-size:12px;letter-spacing:1.5px;text-transform:uppercase;height:40px;padding:0 22px}
.hero-box .btn-outline{margin-top:26px}
/* intro */
.intro-title{left:0;top:722px;width:1200px;text-align:center;font-family:var(--serif);font-size:40px;line-height:1.25;color:var(--ink)}
.intro-text{left:300px;top:840px;width:600px;text-align:center;font-size:17px;line-height:1.55;color:var(--muted)}
.intro-btn{left:470px;top:922px;width:260px;height:52px;color:var(--ink);font-size:13px}
/* about */
.about-bg{left:0;top:1050px;width:1200px;height:670px;background:var(--blush-pale)}
.about-frame{left:122px;top:1186px;width:392px;height:430px;background:var(--white);box-shadow:0 4px 18px rgba(0,0,0,.08)}
.about-photo{left:136px;top:1200px;width:364px;height:402px;background:linear-gradient(135deg,#d9c3a4,#eadbc9 40%,#2fb4a8 75%,#1e9d95)}
.sec-title{font-family:var(--serif);font-size:40px;letter-spacing:2px;text-transform:uppercase;font-weight:400;color:var(--ink)}
.rule{height:1px;background:var(--pink-soft)}
.body-text{font-size:15px;line-height:1.6;color:var(--muted)}
.signature{left:600px;top:1552px;width:190px;height:56px;background:var(--blush)}
/* work with me */
.work-bg{left:0;top:1720px;width:660px;height:560px;background:var(--grey-panel)}
.work-frame{left:540px;top:1818px;width:510px;height:370px;background:var(--white);box-shadow:0 4px 18px rgba(0,0,0,.08)}
.work-photo{left:554px;top:1832px;width:482px;height:342px;background:linear-gradient(135deg,#9c8a78,#e8e2d8 45%,#f4f1ec 70%,#b9c0c8)}
/* praise */
.quote-mark{left:574px;top:2462px;font-family:var(--serif);font-size:80px;line-height:1;color:var(--blush)}
.praise-text{left:290px;top:2520px;width:620px;text-align:center;font-size:16px;line-height:1.6;color:var(--muted)}
.praise-name{left:0;top:2624px;width:1200px;text-align:center;font-size:16px;font-weight:500;color:var(--ink)}
.praise-role{left:0;top:2648px;width:1200px;text-align:center;font-size:14px;color:var(--muted)}
/* podcasts */
.pod-bg{left:0;top:2740px;width:1200px;height:500px;background:var(--blush-pale)}
.card{top:2900px;width:318px;height:290px;background:var(--white);border-radius:40px 0 40px 0;text-align:center;padding-top:30px}
.card .icon{width:56px;height:56px;border-radius:50%;background:var(--pink-soft);margin:0 auto;display:flex;align-items:center;justify-content:center}
.card h3{font-size:15px;font-weight:600;line-height:1.35;margin:22px 34px 0;text-transform:uppercase;color:var(--ink)}
.card p{font-size:13px;line-height:1.5;color:var(--muted);margin:12px 40px 0}
.card .btn-outline{margin-top:18px;height:34px;font-size:11px;border-color:var(--pink-soft);color:var(--ink)}
/* appointment */
.appt-border{left:60px;top:3370px;width:510px;height:430px;border:3px solid var(--pink-soft);border-radius:0 60px 0 60px}
.appt-photo{left:44px;top:3388px;width:510px;height:414px;border-radius:0 60px 0 60px;background:linear-gradient(160deg,#6e5a8a,#c3a47a 35%,#f2eee9 55%,#8a3b3b 85%)}
.field{left:620px;width:434px;height:44px;border:1px solid #D9D9D9;background:var(--white);display:flex;align-items:center;padding-left:14px;font-size:13px;color:#9A9A9A;gap:10px}
.send{left:620px;top:3744px;width:222px;height:42px;background:var(--pink-soft);color:var(--white);font-size:12px;letter-spacing:1px;display:flex;align-items:center;justify-content:center;text-transform:uppercase}
/* footer */
.footer{left:0;top:3924px;width:1200px;height:228px;background:var(--mauve)}
.up{left:574px;top:3896px;width:52px;height:52px;border-radius:50%;background:var(--mauve);display:flex;align-items:center;justify-content:center}
.foot-nav{top:4000px;font-size:14px;letter-spacing:1px;text-transform:uppercase;color:var(--white);font-weight:500}
.copy{left:0;top:4040px;width:1200px;text-align:center;font-size:12px;color:#F3E8EB}
.social{top:4080px;width:32px;height:32px;border-radius:50%;border:2px solid var(--white)}
</style>
</head>
<body>
<div class="abs topline"></div>

<header>
  <div class="abs brand">Dana Whitfield</div>
  <div class="abs nav active" style="left:432px">Work With Me</div>
  <div class="abs nav" style="left:600px">Praise</div>
  <div class="abs nav" style="left:714px">About</div>
  <div class="abs nav" style="left:804px">Podcast</div>
  <div class="abs book-online">BOOK ONLINE</div>
</header>

<section class="hero">
  <div class="abs photo hero-photo" role="img" aria-label="Portrait of the coach in a denim jacket leaning on a wooden fence outdoors"></div>
  <div class="abs hero-shadow"></div>
  <div class="abs hero-box">
    <h1 class="hero-title">Life Coach for<br>Educators</h1>
    <p class="hero-sub">Being Overwhelmed. Being Overcommitted.<br>And not having Work – Life Balance.</p>
    <a class="btn-outline">Book an Appointment</a>
  </div>
</section>

<section class="intro">
  <h2 class="abs intro-title">Why School Leaders Need<br>Balance to Succeed</h2>
  <p class="abs intro-text">DISCOVER the secrets on how to prioritize the items on an overwhelming to-do list to get the job done successfully.</p>
  <a class="abs btn-outline intro-btn">Download Free Guide&nbsp;→</a>
</section>

<section class="about">
  <div class="abs about-bg"></div>
  <div class="abs about-frame"></div>
  <div class="abs about-photo" role="img" aria-label="Portrait of the coach in a teal top resting her chin on her hand"></div>
  <h2 class="abs sec-title" style="left:598px;top:1236px">About Me</h2>
  <div class="abs rule" style="left:600px;top:1300px;width:200px"></div>
  <p class="abs body-text" style="left:600px;top:1324px;width:500px">I'm a Life Coach. I am also a retired Elementary School Principal who loves other educators and everything in education. In my coaching practice, I empower my clients with simple survival skills to succeed at their school and in their life. They have more time, less stress, and yell less.</p>
  <p class="abs body-text" style="left:600px;top:1456px;width:500px">If you would like to learn more about how to manage stress and overwhelm, and how to feel better no matter what the circumstances I am your gal.</p>
  <div class="abs signature" role="img" aria-label="Handwritten signature of Dana Whitfield"></div>
</section>

<section class="work">
  <div class="abs work-bg"></div>
  <h2 class="abs sec-title" style="left:180px;top:1856px">Work With Me</h2>
  <div class="abs rule" style="left:180px;top:1920px;width:200px"></div>
  <p class="abs body-text" style="left:180px;top:1946px;width:330px">I'm a Life Coach. I am also a retired Elementary School Principal who loves other educators and everything in education. In my coaching practice, I empower my clients with simple survival skills to succeed at their school.</p>
  <a class="abs btn-outline" style="left:180px;top:2136px;width:180px;color:var(--ink)">Learn More&nbsp;→</a>
  <div class="abs work-frame"></div>
  <div class="abs work-photo" role="img" aria-label="The coach at a desk with a microphone and laptop recording a session"></div>
</section>

<section class="praise">
  <h2 class="abs sec-title" style="left:0;top:2360px;width:1200px;text-align:center">Praise</h2>
  <div class="abs rule" style="left:520px;top:2424px;width:160px"></div>
  <div class="abs quote-mark">&ldquo;</div>
  <svg class="abs" style="left:150px;top:2530px" width="40" height="24" viewBox="0 0 40 24"><path d="M38 12H3M13 2L3 12l10 10" fill="none" stroke="#B9B9B9" stroke-width="2"/></svg>
  <svg class="abs" style="left:1000px;top:2530px" width="40" height="24" viewBox="0 0 40 24"><path d="M2 12h35M27 2l10 10-10 10" fill="none" stroke="#B9B9B9" stroke-width="2"/></svg>
  <p class="abs praise-text">Working with her gave me clear steps to calm my busy days, plan my week with care and find time again for my family and the things I enjoy most outside of work.</p>
  <div class="abs praise-name">Carla Benton</div>
  <div class="abs praise-role">Weight Coach for Military Moms</div>
</section>

<section class="podcasts">
  <div class="abs pod-bg"></div>
  <h2 class="abs sec-title" style="left:0;top:2788px;width:1200px;text-align:center">Podcats</h2>
  <div class="abs rule" style="left:520px;top:2852px;width:160px"></div>
  <article class="abs card" style="left:124px">
    <div class="icon"><svg width="24" height="30" viewBox="0 0 24 30"><rect x="7" y="2" width="10" height="16" rx="5" fill="#fff"/><path d="M3 14a9 9 0 0 0 18 0M12 23v5M7 28h10" fill="none" stroke="#fff" stroke-width="2"/></svg></div>
    <h3>Mother's Day Can Be Filled With Conflicting</h3>
    <p>It's Mother's Day weekend, and I am traveling to Texas to see my Mom</p>
    <a class="btn-outline">Listen Now&nbsp;→</a>
  </article>
  <article class="abs card" style="left:460px">
    <div class="icon"><svg width="24" height="30" viewBox="0 0 24 30"><rect x="7" y="2" width="10" height="16" rx="5" fill="#fff"/><path d="M3 14a9 9 0 0 0 18 0M12 23v5M7 28h10" fill="none" stroke="#fff" stroke-width="2"/></svg></div>
    <h3>Mother's Day Can Be Filled With Conflicting</h3>
    <p>It's Mother's Day weekend, and I am traveling to Texas to see my Mom</p>
    <a class="btn-outline">Listen Now&nbsp;→</a>
  </article>
  <article class="abs card" style="left:798px">
    <div class="icon"><svg width="24" height="30" viewBox="0 0 24 30"><rect x="7" y="2" width="10" height="16" rx="5" fill="#fff"/><path d="M3 14a9 9 0 0 0 18 0M12 23v5M7 28h10" fill="none" stroke="#fff" stroke-width="2"/></svg></div>
    <h3>Mother's Day Can Be Filled With Conflicting</h3>
    <p>It's Mother's Day weekend, and I am traveling to Texas to see my Mom</p>
    <a class="btn-outline">Listen Now&nbsp;→</a>
  </article>
</section>

<section class="appointment">
  <div class="abs appt-border"></div>
  <div class="abs appt-photo" role="img" aria-label="The coach smiling on a sofa with a laptop in front of a colourful painting"></div>
  <h2 class="abs sec-title" style="left:620px;top:3386px;font-size:36px">Book Appointment</h2>
  <div class="abs rule" style="left:620px;top:3440px;width:200px"></div>
  <div class="abs field" style="top:3466px"><svg width="14" height="14" viewBox="0 0 14 14"><circle cx="7" cy="4" r="3" fill="none" stroke="#C9A3B3" stroke-width="1.4"/><path d="M1 13c1-3 3-4 6-4s5 1 6 4" fill="none" stroke="#C9A3B3" stroke-width="1.4"/></svg>Name</div>
  <div class="abs field" style="top:3524px"><svg width="14" height="14" viewBox="0 0 14 14"><path d="M3 1l2 3-1.5 1.5a8 8 0 0 0 5 5L10 9l3 2-1.5 2.5C6 13 1 8 .5 2.5z" fill="none" stroke="#C9A3B3" stroke-width="1.4"/></svg>Phone</div>
  <div class="abs field" style="top:3582px"><svg width="14" height="12" viewBox="0 0 14 12"><rect x="1" y="1" width="12" height="10" fill="none" stroke="#C9A3B3" stroke-width="1.4"/><path d="M1 1l6 5 6-5" fill="none" stroke="#C9A3B3" stroke-width="1.4"/></svg>Email address</div>
  <div class="abs field" style="top:3640px;height:88px;align-items:flex-start;padding-top:12px">Leave a message</div>
  <div class="abs send">Send Your Message&nbsp;→</div>
</section>

<footer>
  <div class="abs footer"></div>
  <div class="abs up"><svg width="18" height="18" viewBox="0 0 18 18"><path d="M9 16V3M3 9l6-6 6 6" fill="none" stroke="#fff" stroke-width="2"/></svg></div>
  <div class="abs foot-nav" style="left:208px">Home</div>
  <div class="abs foot-nav" style="left:324px">Work With Me</div>
  <div class="abs foot-nav" style="left:520px">Praise</div>
  <div class="abs foot-nav" style="left:652px">About</div>
  <div class="abs foot-nav" style="left:782px">Podcast</div>
  <div class="abs foot-nav" style="left:932px">Book Online</div>
  <div class="abs copy">Copyright © 2020 Dana Whitfield. All Right Reserved</div>
  <div class="abs social" style="left:518px"></div>
  <div class="abs social" style="left:558px"></div>
  <div class="abs social" style="left:598px"></div>
  <div class="abs social" style="left:638px"></div>
</footer>
</body>
</html>
```